Insight Plus. needs Business Cards

For this project, we need business cards (currently have also put a call out for a logo). We are a start-up called Insight Plus. This is our second company (our first one was called Querivance). Traditionally we have been providing market research services across different sectors, primarily financial services and the pharmaceutical industry. However, we now want to go beyond market research to offer more (Plus.)... strategic consulting and big data knowledge management. We want our brand to be approachable, creative, fun but professional.

Target Market(s)

The target audience is a business professional - we are B2B (business to business) and do not sell our services to individuals. The brands we work with are major brands across industries, but primarily automotive, financial and pharmaceutical.

Industry/Entity Type

Market Research

Font styles to use
Serif
Sans Serif
Other font styles liked:
• Calibri

Requirements
Must have
• Be clean, simple, modern
Show our address and phone number and email address and website URL
We do not need to have titles showing.

```html
<!DOCTYPE html>
<html lang="en">
<head>
<meta charset="utf-8">
<title>Insight Plus. Business Cards</title>
<link href="https://fonts.googleapis.com/css2?family=Arimo:wght@400;700&display=swap" rel="stylesheet">
<style>
  :root {
    --backdrop: #e6e4e2;
    --brand-blue: #1553a1;
    --name-blue: #1f64b4;
    --label-blue: #1a4fa0;
    --ink: #3a3a3a;
    --ink-soft: #444444;
    --rule: #4a4a4a;
    --paper: #ffffff;
    --mark-grey: #4d4d4d;
  }
  * { margin: 0; padding: 0; box-sizing: border-box; }
  html, body {
    width: 1200px;
    height: 1000px;
    overflow: hidden;
    background: var(--backdrop);
    font-family: "Arimo", Arial, sans-serif;
  }
  .stage { position: relative; width: 1200px; height: 1000px; }

  .card {
    position: absolute;
    left: 265px;
    width: 665px;
    box-shadow: 0 4px 14px rgba(0,0,0,0.18);
  }
  .card--front { top: 73px; height: 397px; background: var(--brand-blue); }
  .card--back  { top: 532px; height: 398px; background: var(--paper); }

  .front-mark {
    position: absolute;
    left: 282px; top: 92px;
    width: 100px; height: 100px;
    border-radius: 50%;
    background: var(--paper);
  }
  .front-name {
    position: absolute;
    left: 0; right: 0; top: 242px;
    text-align: center;
    color: var(--paper);
    font-weight: 700;
    font-size: 46px;
    letter-spacing: 0.5px;
  }

  .back-mark {
    position: absolute;
    left: 130px; top: 118px;
    width: 84px; height: 84px;
    border-radius: 50%;
    background: var(--mark-grey);
  }
  .back-name {
    position: absolute;
    left: 30px; top: 253px;
    width: 300px;
    text-align: center;
    color: var(--name-blue);
    font-weight: 700;
    font-size: 35px;
  }
  .divider {
    position: absolute;
    left: 352px; top: 84px;
    width: 2px; height: 236px;
    background: var(--rule);
  }
  .contact { position: absolute; left: 377px; top: 92px; color: var(--ink); }
  .person-name { color: var(--name-blue); font-weight: 700; font-size: 20px; }
  .person-role { font-size: 16px; margin-top: 6px; color: var(--ink-soft); }
  .address { font-weight: 700; font-size: 16px; line-height: 22px; margin-top: 26px; }
  .details { margin-top: 20px; font-size: 16px; line-height: 23px; }
  .details .row { display: flex; }
  .details .row--web { margin-top: 13px; }
  .details .label { color: var(--label-blue); width: 66px; }
  .details .row--web .label { width: 68px; }
</style>
</head>
<body>
<main class="stage">
  <section class="card card--front">
    <div class="front-mark"></div>
    <div class="front-name">INSIGHT PLUS.</div>
  </section>

  <section class="card card--back">
    <div class="back-mark"></div>
    <div class="back-name">INSIGHT PLUS.</div>
    <div class="divider"></div>
    <div class="contact">
      <p class="person-name">Daniel Hartwell</p>
      <p class="person-role">Managing Director</p>
      <p class="address">14 Calloway Street<br>Brunswick VIC 3056</p>
      <div class="details">
        <p class="row"><span class="label">Phone:</span><span>+61 400 555 218</span></p>
        <p class="row"><span class="label">Email:</span><span>daniel@insightplus.com</span></p>
        <p class="row row--web"><span class="label">Web:</span><span>www.insightplus.com</span></p>
      </div>
    </div>
  </section>
</main>
</body>
</html>
```